VEXA New York *Luxury Candles*

We need a logo AND package design for a new private label luxury candle company.
I'm an interior decorator. When you enter a space you can perceive design as a 3 dimensional experience. However, the perfect scent in a space makes your experience unforgettable and 4 dimensional. Scents have the power to evoke pleasure and bring back memories.
I want my costumer to have a luxurious experience from the moment they see the package, open it, smell, enjoy and use it to decorate their spaces.
We are looking for a clean design that reads LUX. I'm attaching some pictures for Inspiration.
The candle is approximately 4 inches high 3.5 inches wide (10.3cm high, 9cm wide).

The company's name is

VEXA
New York

Target Market(s)

Women between 27 and 50 who like design, elegance, and beautiful spaces.
They like to indulge and create their safety sanctuary at home.

Industry/Entity Type

It Company

Font styles to use
Sans Serif
Script

Requirements
Must have
• A design for the candle and a design for the gift box + logo
Nice to have
• Simplicity
• Elegance
• Efortless beauty
Should not have
• Many different colors
• Shouldn't be overdone

```html
<!DOCTYPE html>
<html lang="en">
<head>
<meta charset="utf-8">
<title>VEXA New York – Gift Box and Candle Label</title>
<link rel="stylesheet" href="https://fonts.googleapis.com/css2?family=Cinzel:wght@400&family=Lato:wght@400&display=swap">
<style>
  :root {
    --page-bg: #ffffff;
    --box-black: #050505;
    --jar-black: #15151b;
    --label-black: #000000;
    --gold: #d2a640;
    --gold-light: #f6e08e;
    --gold-deep: #a9791b;
    --band-yellow: #e8c21a;
    --caption-ink: #111111;
  }
  * { margin: 0; padding: 0; box-sizing: border-box; }
  html, body {
    width: 1200px;
    height: 611px;
    overflow: hidden;
    background: var(--page-bg);
  }
  .canvas { position: relative; width: 1200px; height: 611px; }

  /* Shared brand mark: name, city, plain ring */
  .mark {
    position: absolute;
    display: flex;
    flex-direction: column;
    align-items: center;
    justify-content: center;
    color: var(--gold);
    font-family: "Cinzel", serif;
    font-weight: 400;
  }
  .mark::before {
    content: "";
    position: absolute;
    inset: 8px;
    border: 1px solid var(--gold);
    border-radius: 50%;
  }
  .mark__name { font-size: 28px; letter-spacing: 1px; line-height: 1; }
  .mark__city { font-size: 8px; letter-spacing: 0.5px; margin-top: 12px; }

  /* Gift box front panel */
  .gift-box {
    position: absolute;
    left: 110px;
    top: 105px;
    width: 248px;
  }
  .gift-box__face {
    position: relative;
    height: 324px;
    background: var(--box-black);
  }
  .gift-box__frame {
    position: absolute;
    inset: 8px;
    border: 2px solid var(--gold);
  }
  .gift-box__face .mark { left: 55px; top: 62px; width: 138px; height: 138px; }
  .gift-box__base {
    height: 35px;
    background: linear-gradient(90deg, var(--gold-deep), var(--band-yellow) 40%, var(--gold-light) 70%, var(--band-yellow));
  }

  /* Candle jar wrap */
  .candle-wrap {
    position: absolute;
    left: 385px;
    top: 158px;
    width: 262px;
    height: 360px;
    background: var(--jar-black);
    border-radius: 6px 6px 22px 22px;
  }
  .candle-wrap__rule {
    position: absolute;
    left: 8px;
    right: 8px;
    height: 1px;
    background: var(--gold);
  }
  .candle-wrap__rule--top { top: 58px; }
  .candle-wrap__rule--top-inner { top: 64px; }
  .candle-wrap__rule--bottom { top: 330px; }
  .candle-wrap .mark { left: 62px; top: 115px; width: 138px; height: 138px; }

  /* Standalone mark on white */
  .brand-mark.mark { left: 667px; top: 198px; width: 134px; height: 136px; }

  /* Flat candle label */
  .label-size {
    position: absolute;
    left: 972px;
    top: 108px;
    font-family: "Lato", sans-serif;
    font-size: 12px;
    color: var(--caption-ink);
  }
  .candle-label {
    position: absolute;
    left: 840px;
    top: 132px;
    width: 280px;
    height: 320px;
    background: var(--label-black);
  }
  .candle-label__frame {
    position: absolute;
    inset: 9px;
    border: 2px solid var(--gold);
  }
  .candle-label .mark { left: 76px; top: 63px; width: 138px; height: 139px; }
</style>
</head>
<body>
  <main class="canvas">
    <section class="gift-box" aria-label="VEXA New York gift box front">
      <div class="gift-box__face">
        <div class="gift-box__frame"></div>
        <div class="mark">
          <span class="mark__name">VEXA</span>
          <span class="mark__city">New York</span>
        </div>
      </div>
      <div class="gift-box__base"></div>
    </section>

    <section class="candle-wrap" aria-label="VEXA New York candle jar">
      <div class="candle-wrap__rule candle-wrap__rule--top"></div>
      <div class="candle-wrap__rule candle-wrap__rule--top-inner"></div>
      <div class="mark">
        <span class="mark__name">VEXA</span>
        <span class="mark__city">New York</span>
      </div>
      <div class="candle-wrap__rule candle-wrap__rule--bottom"></div>
    </section>

    <div class="brand-mark mark">
      <span class="mark__name">VEXA</span>
      <span class="mark__city">New York</span>
    </div>

    <p class="label-size">10.3cm high, 9cm wide</p>

    <section class="candle-label" aria-label="VEXA New York candle label">
      <div class="candle-label__frame"></div>
      <div class="mark">
        <span class="mark__name">VEXA</span>
        <span class="mark__city">New York</span>
      </div>
    </section>
  </main>
</body>
</html>
```